TunedLobe need a flyer designed for musician hearing protection products

TunedLobe is a company who specializes in custom hearing protection for the general public and musicians. In addition we offer in-ear monitors for musicians. We need a flyer designed that we can distribute in concert halls, recording studios, musicians, showing the products that we offer, services provided. THe flyer needs to be catchy to get peoples attention and informative at the same time. Currently we are using Chatterbox as the web page (www.tunedlobe-example.com). The manufacturers that we work with are: www.qrvmolds-example.com www.harbinfield-example.com www.plovimetrics-example.com
I am sorry I forgot to add that the flyer will be double sided. On the other side I would like to have a noise exposure chart showing the damage that you would get from different noise exposed situations. There are some charts on the internet but obviously I would like this one to be on a creative side, and contact information.
This will give you an idea of the products that we offer to the public.
Musicians, sounds engineers, general public attending concerts
Internet

```html
<!DOCTYPE html>
<html lang="en">
<head>
<meta charset="utf-8">
<title>TunedLobe Flyer – Front</title>
<link href="https://fonts.googleapis.com/css2?family=Arimo:wght@400;700&family=Source+Sans+3:wght@400;600;700&display=swap" rel="stylesheet">
<style>
  :root {
    --ink: #1a1a1a;
    --charcoal: #2b2b2b;
    --cyan: #3ec5ef;
    --stone: #b9b6a9;
    --paper: #ffffff;
    --muted: #d9d9d9;
  }
  * { box-sizing: border-box; margin: 0; padding: 0; }
  html, body { width: 879px; height: 1200px; overflow: hidden; background: #e6e6e6; }
  .flyer {
    position: relative; width: 879px; height: 1200px; background: var(--paper);
    font-family: "Source Sans 3", sans-serif; color: var(--ink); overflow: hidden;
  }
  .header {
    position: absolute; left: 0; top: 0; width: 879px; height: 351px;
    background: radial-gradient(ellipse at 35% 30%, #5a5a5a 0%, #333 40%, #111 100%);
  }
  .brand {
    position: absolute; left: 60px; top: 150px; display: flex; align-items: center; gap: 16px;
  }
  .brand-dot { width: 22px; height: 22px; border-radius: 50%; background: var(--cyan); }
  .brand-name { font-size: 52px; font-weight: 600; color: #fff; letter-spacing: 0.5px; }
  .tagline {
    position: absolute; left: 481px; top: 106px; width: 390px;
    font-family: "Arimo", sans-serif; font-size: 27px; line-height: 1.2; color: #fff;
  }
  .services {
    position: absolute; left: 44px; top: 297px; font-size: 19px; font-weight: 600; color: var(--cyan);
  }
  .band {
    position: absolute; left: 0; top: 351px; width: 879px; height: 281px; background: var(--cyan);
  }
  .product { position: absolute; top: 34px; }
  .product-photo { height: 183px; border: 2px solid #222; border-radius: 18px; }
  .product-name {
    margin-top: 6px; margin-left: 12px; font-size: 17px; font-weight: 700;
    line-height: 1.2; text-transform: uppercase; color: var(--charcoal);
  }
  .p1 { left: 30px; } .p1 .product-photo { width: 261px; background: linear-gradient(135deg,#efe9d8,#c9bfb0 60%,#5a2a22); }
  .p2 { left: 317px; } .p2 .product-photo { width: 255px; background: linear-gradient(135deg,#f1ecdc,#e4e0d2 55%,#4f6fb0); }
  .p3 { left: 589px; } .p3 .product-photo { width: 259px; background: linear-gradient(135deg,#f2edd9,#d6cfc0 50%,#d56ca8 75%,#c7dd4a); }
  .about {
    position: absolute; left: 50px; top: 669px; width: 437px; height: 329px;
    background: var(--stone); border-radius: 14px; padding: 20px 18px 0 18px;
    font-size: 13.2px; line-height: 1.4; color: #222;
  }
  .about .wrap-body { float: right; width: 170px; height: 82px; }
  .about .wrap-tail { float: right; clear: right; width: 100px; height: 40px; }
  .about h2 { font-size: 18px; font-weight: 700; margin-bottom: 2px; }
  .about p { margin-bottom: 7px; }
  .hl { color: #fff; font-weight: 700; }
  .bubble-ring {
    position: absolute; left: 332px; top: 628px; width: 176px; height: 176px; z-index: 2;
  }
  .bubble-photo {
    position: absolute; left: 340px; top: 636px; width: 160px; height: 124px; z-index: 3;
    border-radius: 50%; background: radial-gradient(circle at 45% 45%, #a24b2a, #5a2a1e 45%, #1b1f3a 90%);
  }
  .benefits {
    position: absolute; left: 530px; top: 672px; width: 306px; height: 395px;
    border-radius: 16px; background: linear-gradient(180deg,#3a3a3a,#121212 35%,#1e1e1e);
    padding: 20px 20px 0 20px; font-size: 13.4px; line-height: 1.42; color: #eee; text-align: justify;
  }
  .benefits .intro { color: var(--cyan); font-size: 15.5px; text-align: center; line-height: 1.3; margin-bottom: 20px; }
  .benefits p { margin-bottom: 18px; }
  .benefits .term { color: var(--cyan); }
  .promise {
    position: absolute; left: 63px; top: 1018px; font-family: "Arimo", sans-serif;
    font-size: 37px; line-height: 1.18; color: var(--ink);
  }
  .call {
    position: absolute; left: 523px; top: 1080px; font-family: "Arimo", sans-serif; font-size: 26px;
  }
  .rule { position: absolute; left: 0; top: 1150px; width: 879px; height: 4px; background: var(--muted); }
  .footer {
    position: absolute; left: 0; top: 1158px; width: 879px; height: 42px; background: #1c1c1c;
    color: #fff; font-family: "Arimo", sans-serif; font-size: 27px; text-align: center; line-height: 42px;
  }
</style>
</head>
<body>
<main class="flyer">
  <header class="header">
    <div class="brand"><span class="brand-dot"></span><span class="brand-name">TunedLobe</span></div>
    <p class="tagline">Your one stop source for<br>custom audio earpieces,<br>Bluetooth earpieces &amp;<br>hearing protection.</p>
    <p class="services">Ear Molds • Ear Protection • In-Ear Monitors</p>
  </header>

  <section class="band">
    <div class="product p1">
      <div class="product-photo" role="img" aria-label="Photo of a custom-molded Bluetooth earpiece"></div>
      <p class="product-name">Custom Bluetooth<br>Earpieces</p>
    </div>
    <div class="product p2">
      <div class="product-photo" role="img" aria-label="Photo of blue custom audio ear molds with white earbuds"></div>
      <p class="product-name">Custom Audio<br>Earpieces</p>
    </div>
    <div class="product p3">
      <div class="product-photo" role="img" aria-label="Photo of colourful corded hearing protection plugs"></div>
      <p class="product-name">Custom Hearing<br>Protection</p>
    </div>
  </section>

  <section class="about">
    <span class="wrap-body"></span>
    <span class="wrap-tail"></span>
    <h2>About Us</h2>
    <p><span class="hl">TunedLobe</span> products combine the latest in acoustic technology and over five decades of experience in crafting custom fit products for the human ear. “Customs” as they are most commonly referred to are primarily used by the professional on-stage musician but have also gained popularity with audiophiles looking for a critical listening earpiece. Athletes looking for an earphone that stays in the ear can also benefit from a TunedLobe made product.</p>
    <p>All <span class="hl">TunedLobe</span> products require an ear-impression<br>Custom monitors are a great choice for those with hard to fit ears and can offer a superior seal for particular anatomies.</p>
    <p>TunedLobe monitors are made to order and offer virtually unlimited customization options.</p>
  </section>

  <svg class="bubble-ring" viewBox="0 0 176 176" aria-hidden="true">
    <path d="M88 6 C140 6 172 34 172 72 C172 110 140 136 96 138 L66 172 L70 136 C30 128 4 104 4 72 C4 34 36 6 88 6 Z" fill="#1a1a1a" stroke="#3ec5ef" stroke-width="5"/>
  </svg>
  <div class="bubble-photo" role="img" aria-label="Photo of a performer singing on stage"></div>

  <section class="benefits">
    <p class="intro">With our TunedLobe Bluetooth Earpiece, your Bluetooth will be more comfortable, secure and will sound better than ever before.</p>
    <p><span class="term">Comfort</span>: It's molded to your ear, it follows every contour perfectly.</p>
    <p><span class="term">Security</span>: Your bluetooth device will fit perfectly with no jiggle or need to instantly re-position. It stays in your ear so you can kiss the earwire goodbye!</p>
    <p><span class="term">Better Sound</span>: The earpiece perfectly follows the curves of your ear and blocks outside noises better while directing the Bluetooth sound right into your ear canal. Some have reported turning their volume down from full blast to 2 bars and hearing their calls better!</p>
  </section>

  <p class="promise">Perfect fit, every time...<br>GUARANTEED</p>
  <p class="call">Call Us : 012-555-0147</p>
  <div class="rule"></div>
  <footer class="footer">www.tunedlobe-example.com</footer>
</main>
</body>
</html>
```